NORDIC HERON WEBSITE DESIGN

We need a website designed for Nordic Heron Timepieces, its a watch brand which originated from switzerland, you will get data on nordic heron on www.nordicherontime.example.

The website needs to be a combination of the following websites.

http://www.kolvarine.example/int-en/home
http://www.dunstable-ferro.example/en/

The look of the website should be very luxury and classy, should look like a swiss website with a lot of swiss imagery of mountains, etc.

The website will be an online shopping website, so should have add to card, shopping link etc...

Target Market(s)

Successful people who have arrived in LIFE

Age : 30-45 managerial class people

Industry/Entity Type

Online Shopping

Font styles to use
Sans Serif

Colors

Designer to choose colors to be used in the design.

Requirements
Must have
• Flash banners on the homepage
Swiss feel on the website is a must

```html
<!DOCTYPE html>
<html lang="en">
<head>
<meta charset="utf-8">
<title>Nordic Heron Timepieces</title>
<link href="https://fonts.googleapis.com/css2?family=Abel&family=Exo+2:wght@400;700;800&family=Oswald:wght@600&family=Roboto:wght@300;400&display=swap" rel="stylesheet">
<style>
:root{
  --page:#201e26;
  --header:#3a3946;
  --header-dark:#2c2b37;
  --nav:#302f3c;
  --panel:#000;
  --field:#2a2933;
  --line:#6a6790;
  --gold:#c8a85e;
  --text:#e9e8ef;
  --muted:#8a8898;
  --dim:#5d5b68;
  --red:#d3213a;
}
*{box-sizing:border-box;margin:0;padding:0}
html,body{width:932px;height:1200px;overflow:hidden}
body{position:relative;background:var(--page);font-family:"Roboto",sans-serif;color:var(--text)}
a{color:inherit;text-decoration:none}
.abs{position:absolute}

/* header */
.site-header{position:absolute;left:0;top:0;width:932px;height:88px;background:var(--header)}
.main-nav{position:absolute;left:0;top:88px;width:932px;height:34px;background:var(--nav);border-top:1px solid #4a4958;border-bottom:1px solid #1a1920}
.account-links{position:absolute;left:73px;top:17px;font-size:11px;color:#fff;width:234px;border-bottom:1px solid #5a5968;padding-bottom:6px}
.account-links .or{color:var(--dim);font-size:9px}
.search{position:absolute;left:70px;top:49px;width:238px;height:22px;display:flex}
.search .field{flex:1;background:var(--field);border:1px solid #4b4a58;font-size:10px;font-style:italic;color:#ddd;padding:5px 4px}
.search .go{width:38px;background:#000;display:flex;align-items:center;justify-content:center}
.top-links{position:absolute;left:626px;top:17px;width:240px;font-size:10px;color:#fff;border-bottom:1px solid #5a5968;padding-bottom:6px}
.top-links span.sep{color:var(--dim);margin:0 4px}
.cart{position:absolute;left:626px;top:47px;width:240px;height:22px;background:var(--field);display:flex;align-items:center;font-size:10px;font-style:italic}
.cart .icon{width:24px;height:22px;background:var(--gold);display:flex;align-items:center;justify-content:center;margin-right:12px}
.nav-item{position:absolute;top:9px;font-size:12px;color:#8d8ba3}
.nav-item.active{color:var(--gold)}
.nav-sep{position:absolute;top:4px;width:1px;height:24px;background:#4c4b5a}
.logo-diamond{position:absolute;left:467px;top:86px}
.brand{position:absolute;left:395px;top:88px;width:144px;text-align:center;font-family:"Exo 2",sans-serif;font-size:13px;letter-spacing:1px;color:#fff}

/* slider */
.slider-top{position:absolute;left:70px;top:143px;width:796px;height:81px;background:#0b0b0e}
.slider-top .bar{position:absolute;left:32px;top:26px;width:726px;height:28px;background:#15171a}
.slider{position:absolute;left:70px;top:224px;width:796px;height:245px;background:#000;overflow:hidden;border-top:1px solid #222}
.slider h1{position:absolute;left:57px;top:30px;font-family:"Abel",sans-serif;font-weight:400;font-size:28px;color:#fff}
.slider p{position:absolute;left:57px;top:72px;width:280px;font-size:10px;line-height:16px;color:#3d3b47;font-weight:300}
.btn-cart-lg{position:absolute;left:57px;top:136px}
.slide-photo{position:absolute;left:465px;top:6px;width:300px;height:234px;border-radius:40px;background:radial-gradient(ellipse at 40% 55%,#d9d9dc 0,#8d8d92 30%,#3a2a2a 60%,#000 80%)}
.dots{position:absolute;left:24px;top:255px}
.arrow-nav{position:absolute;top:166px}

/* products */
.section-title{position:absolute;left:71px;top:488px;font-family:"Exo 2",sans-serif;font-weight:800;font-variant:small-caps;font-size:18px;color:#fff;display:flex;align-items:center;gap:8px}
.section-rule{position:absolute;left:70px;top:517px;width:787px;height:2px;background:var(--line)}
.product{position:absolute;top:520px;width:150px;height:231px;background:var(--panel);border-top:2px solid var(--line)}
.product .photo{position:absolute;left:35px;top:18px;width:80px;height:115px;border-radius:20px;background:linear-gradient(180deg,#9a9ca3,#2a3550 50%,#9a9ca3)}
.product h3{position:absolute;left:8px;top:145px;font-family:"Exo 2",sans-serif;font-weight:700;font-size:11.5px;color:#fff}
.product .desc{position:absolute;left:8px;top:172px;font-size:8px;color:var(--muted)}
.product .price{position:absolute;left:8px;top:194px;font-family:"Exo 2",sans-serif;font-size:14px;color:var(--gold)}
.product .add{position:absolute;left:82px;top:193px;width:68px;height:18px;background:#2e2d39;font-size:7px;color:#fff;display:flex;align-items:center;padding-left:20px;clip-path:polygon(9px 0,100% 0,100% 100%,9px 100%,0 50%)}

/* promo */
.promo{position:absolute;top:775px;height:86px;background:linear-gradient(90deg,#0e0e14,#1a1a22 60%,#0c0c10);border:1px solid #3a3946}
.promo .t1{position:absolute;left:40px;top:26px;font-family:"Abel",sans-serif;font-size:19px;color:#fff;letter-spacing:.5px}
.promo .t2{position:absolute;left:154px;top:45px;font-family:"Abel",sans-serif;font-size:11px;color:#fff}
.promo .t2 b{font-family:"Exo 2",sans-serif;font-size:17px;font-weight:800}
.promo .photo{position:absolute;top:8px;width:100px;height:78px;border-radius:50px 50px 0 0;background:radial-gradient(circle at 50% 55%,#ddd 0,#333 45%,#111 70%)}

/* footer */
.site-footer{position:absolute;left:0;top:918px;width:932px;height:282px;background:#000;border-top:2px solid var(--line)}
.to-top{position:absolute;left:437px;top:888px;width:60px;height:60px}
.to-top span{position:absolute;left:0;top:28px;width:60px;text-align:center;font-size:7px;color:#fff}
.news{position:absolute;left:78px;top:940px;font-size:10px;color:var(--muted);display:flex;align-items:center;gap:8px}
.news b{font-family:"Exo 2",sans-serif;color:#fff;font-size:11px}
.newsletter{position:absolute;left:514px;top:937px;display:flex;align-items:center;font-size:10px;color:var(--muted)}
.newsletter .field{margin-left:12px;width:180px;height:22px;background:#2f2e3a;display:flex;align-items:center;font-size:10px;font-style:italic;color:#fff}
.newsletter .field svg{margin:0 8px}
.newsletter .go{width:40px;height:22px;background:#3b3a48;margin-left:4px;display:flex;align-items:center;justify-content:center}
.col{position:absolute;top:996px}
.col h4{font-family:"Abel",sans-serif;font-weight:400;font-size:15px;color:#fff;margin-bottom:8px}
.col li{list-style:none;font-size:10px;color:var(--muted);line-height:16px}
.col li::before{content:"· ";color:var(--dim)}
.col p{font-size:10px;color:var(--muted);line-height:16px;width:200px}
.col p.email span{color:#fff}
.follow{position:absolute;left:458px;top:1124px;display:flex;align-items:center;gap:9px;font-family:"Abel",sans-serif;font-size:13px;color:#fff}
.follow i{display:block;width:24px;height:24px;border-radius:50%;background:#3a3946}
.foot-brand{position:absolute;left:740px;top:1060px;width:112px;text-align:center;font-family:"Exo 2",sans-serif;font-size:13px;letter-spacing:1px;color:#fff}
.copyright{position:absolute;left:68px;top:1173px;font-size:10px;color:var(--muted)}
</style>
</head>
<body>

<header class="site-header">
  <div class="account-links"><a href="#">Login</a> <span class="or">or</span> <a href="#">Create an account</a></div>
  <form class="search"><div class="field">Search...</div><div class="go"><svg width="8" height="9"><path d="M0 0L8 4.5L0 9Z" fill="#c8a85e"/></svg></div></form>
  <div class="top-links"><a href="#">My Account</a><span class="sep">|</span><a href="#">Shopping Cart</a><span class="sep">|</span><a href="#">Login</a></div>
  <div class="cart"><div class="icon"><svg width="14" height="12"><path d="M0 1H3L5 8H12L13 3H4" stroke="#fff" stroke-width="1.5" fill="none"/><circle cx="6" cy="10.5" r="1.2" fill="#fff"/><circle cx="11" cy="10.5" r="1.2" fill="#fff"/></svg></div>Cart empty</div>
</header>

<nav class="main-nav">
  <span class="nav-sep" style="left:71px"></span>
  <a class="nav-item active" style="left:95px">Home</a>
  <span class="nav-sep" style="left:150px"></span>
  <a class="nav-item" style="left:176px">Q7 ▾</a>
  <span class="nav-sep" style="left:222px"></span>
  <a class="nav-item" style="left:250px">Features ▾</a>
  <span class="nav-sep" style="left:330px"></span>
  <span class="nav-sep" style="left:593px"></span>
  <a class="nav-item" style="left:617px">ShopHall ▾</a>
  <span class="nav-sep" style="left:707px"></span>
  <a class="nav-item" style="left:732px">Blog</a>
  <span class="nav-sep" style="left:780px"></span>
</nav>

<svg class="abs" style="left:382px;top:0" width="170" height="170" aria-hidden="true">
  <path d="M85 2L168 85L85 168L2 85Z" fill="#26252f" stroke="#45444f"/>
</svg>
<div class="brand" style="top:70px">NORDIC HERON</div>
<svg class="abs" style="left:455px;top:36px" width="24" height="24" aria-hidden="true"><rect x="2" y="2" width="20" height="20" fill="#d3213a"/></svg>

<section class="slider-top"><div class="bar"></div></section>
<svg class="arrow-nav" style="left:50px" width="40" height="40" aria-hidden="true"><path d="M20 2L38 20L20 38L2 20Z" fill="#000"/><path d="M23 13L16 20L23 27" stroke="#c8a85e" stroke-width="4" fill="none"/></svg>
<svg class="arrow-nav" style="left:846px" width="40" height="40" aria-hidden="true"><path d="M20 2L38 20L20 38L2 20Z" fill="#000"/><path d="M17 13L24 20L17 27" stroke="#c8a85e" stroke-width="4" fill="none"/></svg>

<section class="slider">
  <svg class="abs" style="left:0;top:0" width="796" height="245" aria-hidden="true">
    <path d="M40 6L70 36L40 66L10 36Z" fill="#1a1a1e"/>
    <path d="M335 95L375 135L335 175L295 135Z" fill="#1a1a1e"/>
    <path d="M300 150L345 195L300 240L255 195Z" fill="#141418"/>
    <path d="M230 165L260 195L230 225L200 195Z" fill="#101014"/>
    <path d="M380 160L400 180L380 200L360 180Z" fill="#161619"/>
    <path d="M520 0L560 40L520 80L480 40Z" fill="#111114"/>
  </svg>
  <h1>Phasellus at</h1>
  <p>Quisque auctor lacinia convallis. Curabitur nec magna orci, quis mollis justo. Nullam adipiscing ultricies vestibulum. Curabitur eu neque velit. Aenea...</p>
  <a class="btn-cart-lg" href="#"><svg width="175" height="34"><path d="M17 0H175L158 34H0Z" fill="#4c4b5e"/><path d="M17 0L34 17L17 34L0 17Z" fill="#6a6888"/><text x="35" y="24" font-family="Oswald, sans-serif" font-weight="600" font-size="16" fill="#c8a85e">ADD TO CART</text></svg></a>
  <div class="slide-photo" role="img" aria-label="Three luxury wristwatches with white, black and red leather straps"></div>
  <svg class="dots" style="top:202px" width="90" height="14" aria-hidden="true"><path d="M7 0L14 7L7 14L0 7Z" fill="none" stroke="#c8a85e"/><path d="M7 4L10 7L7 10L4 7Z" fill="#c8a85e"/><path d="M27 3L31 7L27 11L23 7Z" fill="#4c4b6a"/><path d="M47 3L51 7L47 11L43 7Z" fill="#4c4b6a"/><path d="M67 3L71 7L67 11L63 7Z" fill="#4c4b6a"/></svg>
</section>

<h2 class="section-title"><svg width="9" height="9"><path d="M4.5 0L9 4.5L4.5 9L0 4.5Z" fill="#fff"/></svg>New produce</h2>
<div class="section-rule"></div>

<article class="product" style="left:74px"><div class="photo" role="img" aria-label="Steel diver watch with blue bezel"></div><h3>Rhoncus sodales</h3><div class="desc">Quisque auctor lacinia conva...</div><div class="price">$120.00</div><a class="add" href="#">ADD TO CART</a></article>
<article class="product" style="left:232px"><div class="photo" role="img" aria-label="Steel diver watch with blue bezel"></div><h3>Dictum sodale</h3><div class="desc">Quisque auctor lacinia conva...</div><div class="price">$116.00</div><a class="add" href="#">ADD TO CART</a></article>
<article class="product" style="left:390px"><div class="photo" role="img" aria-label="Steel chronograph watch with black dial"></div><h3>Lacinia malesuada</h3><div class="desc">Quisque auctor lacinia conva...</div><div class="price">$116.00</div><a class="add" href="#">ADD TO CART</a></article>
<article class="product" style="left:548px"><div class="photo" role="img" aria-label="Steel watch with blue dial"></div><h3>Tortor suscipit</h3><div class="desc">Quisque auctor lacinia conva...</div><div class="price">$116.00</div><a class="add" href="#">ADD TO CART</a></article>
<article class="product" style="left:706px"><div class="photo" role="img" aria-label="Steel watch with blue dial"></div><h3>Hendrerit et</h3><div class="desc">Quisque auctor lacinia conva...</div><div class="price">$116.00</div><a class="add" href="#">ADD TO CART</a></article>

<aside class="promo" style="left:70px;width:389px"><div class="t1">BEST WATCHES</div><div class="t2">FOR <b>MEN</b></div><div class="photo" style="left:265px" role="img" aria-label="Black chronograph watch"></div></aside>
<aside class="promo" style="left:473px;width:384px"><div class="t1">BEST WATCHES</div><div class="t2">FOR <b>MEN</b></div><div class="photo" style="left:265px" role="img" aria-label="Black chronograph watch"></div></aside>

<footer class="site-footer"></footer>
<a class="to-top" href="#"><svg width="60" height="60"><path d="M30 0L60 30L30 60L0 30Z" fill="#3a3946"/><path d="M30 14V22M27 17L30 14L33 17" stroke="#fff" fill="none"/></svg><span>GO TO TOP</span></a>

<div class="news"><svg width="9" height="9"><path d="M4.5 0L9 4.5L4.5 9L0 4.5Z" fill="#fff"/></svg><b>News</b>Risus quis tortor rhoncus</div>
<form class="newsletter">Sign up for Newsletter<div class="field"><svg width="16" height="11"><rect x="0.5" y="0.5" width="15" height="10" fill="none" stroke="#c8a85e"/><path d="M1 1L8 6L15 1" stroke="#c8a85e" fill="none"/></svg>Type your email</div><div class="go"><svg width="7" height="8"><path d="M0 0L7 4L0 8Z" fill="#c8a85e"/></svg></div></form>

<div class="col" style="left:76px"><h4>Information</h4><ul><li>Fusce hen</li><li>Proin imper</li><li>Sed non sem</li><li>Nunc vel</li></ul></div>
<div class="col" style="left:204px"><h4>Assistance</h4><ul><li>Fusce hen</li><li>Proin imper</li><li>Sed non sem</li><li>Nunc vel</li></ul></div>
<div class="col" style="left:331px"><h4>My account</h4><ul><li>Fusce hen</li><li>Proin imper</li><li>Sed non sem</li><li>Nunc vel</li></ul></div>
<div class="col" style="left:458px"><h4>Location</h4>
  <p>Lorem ipsum dolor sit amet, consectetur adipisicing elit...</p>
  <p style="margin-top:4px">Phone: +123 456 789</p>
  <p>Fax: +123 456 788</p>
  <p class="email">Email: <span>contact@harbinwatch.example</span></p>
</div>
<div class="follow">Follow Us On <i></i><i></i><i></i><i></i></div>

<svg class="abs" style="left:784px;top:1010px" width="36" height="36" aria-hidden="true"><rect x="3" y="3" width="30" height="30" fill="#d3213a"/></svg>
<div class="foot-brand">NORDIC HERON</div>

<div class="copyright">Copyright © 2014</div>
</body>
</html>
```